Harborlight Unity Collective Sponsorship

FULL PROJECT DESCRIPTION PROVIDED IN PDF AND WORD DOC (UPLOADED).

Harborlight Unity Collective is looking for an updated sponsorship package design – included in the shared information is our sponsorship packaged used in 2017, 2018, and 2019.

The mission of Harborlight Unity Collective is to create opportunities for integrating and promoting visibility for the lesbian. gay, bisexual and transgender community; promoting equal rights and diversity through public education and the arts; provide safe opportunities and venues for people to come out with the ability to express and celebrate their sexual identities.

Some images (because of their size) are not allowed to be uploaded... use the following link to access the full library of images, reference documents, and the full outline: https://files.vexorabox.net/shared/7qTmW3zK9-4rbLnYcP2sVdHgE6uJaXf0N?mode=view

Sponsorship packet design details:
Final file type: .pdf and/or .ai/.eps
Orientation: Preferably landscape but not opposed to a portrait design.
Page count: estimated 6 with current content (not opposed to 8 pages)
Size: 8.5”x11”
Full bleed

Images:
Images for this design are shared in a folder “images for use in sponsorship packet” – please feel free to choose them as you see fit and we can make any notes after the first draft.

Creative Reference:
Additionally, provided are a few sponsorship packages that we like and feel that you might be able to take inspiration from – these are in a folder named “sponsorship packets we like”
Updates

I've updated all of the details of this project and would like to have completed asap. Thank you.

Target Market(s)

Primarily our target market is local and regional businesses that are interested in supporting GlowFair through sponsorship or might be interested in advertising opportunities.

Industry/Entity Type

LGBT

Font styles to use
Serif
Sans Serif

Colors

Designer to choose colors to be used in the design.

Requirements
Must have
• All sponsorship details

```html
<!DOCTYPE html>
<html lang="en">
<head>
<meta charset="utf-8">
<title>Harborlight Unity Collective – 2020 Sponsorship Packet</title>
<link rel="stylesheet" href="https://fonts.googleapis.com/css2?family=Rubik:wght@400;500;700;800&family=Inter:wght@300;400;600;700&display=swap">
<style>
  :root{
    --purple:#6a4c93;
    --purple-deep:#5a3f82;
    --coral:#f65a5f;
    --yellow:#fcbf2e;
    --ink:#2b2b2b;
    --bg:#f4f3f9;
    --white:#ffffff;
    --grey:#ececef;
    --rainbow:linear-gradient(90deg,#e53935,#fb8c00,#fdd835,#43a047,#1e88e5,#8e24aa);
  }
  *{box-sizing:border-box;margin:0;padding:0}
  html,body{width:1200px;height:3008px;overflow:hidden;background:var(--bg)}
  body{font-family:"Inter",Arial,sans-serif;color:var(--ink)}
  .board{position:absolute;left:0;top:0;width:1028px;height:2577px;transform:scale(1.16732);transform-origin:0 0;overflow:hidden;background:var(--bg)}
  .board-band{position:absolute;inset:0;background:var(--white);clip-path:polygon(0 925px,100% 695px,100% 1415px,0 1740px)}
  .page-label{position:absolute;left:197px;font-family:"Inter",Arial,sans-serif;font-weight:400;font-size:19px;letter-spacing:-.2px;color:#222}

  .sheet{position:absolute;background:var(--white);overflow:hidden;box-shadow:0 6px 18px rgba(60,50,90,.12)}
  .abs{position:absolute}
  .photo{position:absolute}
  .dot{position:absolute;border-radius:50%}
  .h-display{font-family:"Rubik",Arial,sans-serif;font-weight:700;letter-spacing:-.3px}
  .copy{font-size:6.4px;line-height:10.8px;color:var(--ink)}
  .copy p{margin-bottom:10px}

  /* cover */
  .cover{left:320px;top:70px;width:370px;height:478px}
  .cover-bottom{left:0;bottom:0;width:100%;height:12px;background:var(--yellow)}
  .cover-year{font-family:"Rubik",Arial,sans-serif;color:var(--white);text-align:center;transform:rotate(14deg)}
  .cover-year .year{font-weight:700;font-size:22px;line-height:22px}
  .cover-year .sub{font-weight:500;font-size:8px;line-height:10px;letter-spacing:.8px}
  .brand{font-family:"Rubik",Arial,sans-serif;font-weight:700;font-size:13px;line-height:14px;color:var(--purple);width:120px}
  .brand-rule{width:1px;height:34px;background:#999}
  .event-line{font-family:"Inter",Arial,sans-serif;font-size:6.8px;line-height:9px;color:#444}
  .event-line b{font-weight:700;font-style:italic;letter-spacing:.2px}
  .event-line i{font-size:5.8px}

  /* page 1 */
  .p1{left:300px;top:617px;width:428px;height:550px}
  .p1 .title{left:26px;top:240px;font-size:27px;line-height:26px;color:var(--purple)}
  .p1 .salute{left:26px;top:302px;font-size:6.8px;font-weight:700}
  .p1 .col-left{left:26px;top:322px;width:180px}
  .p1 .col-right{left:217px;top:203px;width:190px}
  .sign{font-weight:700}

  /* page 2 */
  .p2{left:304px;top:1263px;width:424px;height:545px}
  .p2 .h-support{left:31px;top:185px;font-size:13.5px;line-height:16px;color:var(--coral);font-weight:500}
  .p2 .para-support{left:31px;top:224px;width:190px}
  .p2 .h-build{right:34px;top:330px;font-size:13.5px;line-height:16px;color:var(--purple);font-weight:500;text-align:right}
  .p2 .para-build{right:34px;top:367px;width:200px;text-align:right}
  .p2 .grey{inset:0;background:var(--grey);clip-path:polygon(0 340px,100% 215px,100% 100%,0 100%)}
  .p2 .terms{inset:0;background:var(--purple);clip-path:polygon(0 472px,100% 437px,100% 100%,0 100%)}
  .p2 .terms-head{left:23px;top:482px;font-size:6.4px;line-height:8px;font-weight:700;color:var(--white)}
  .p2 .terms-copy{left:83px;top:480px;width:312px;font-size:5.9px;line-height:9.2px;color:var(--white)}
  .ring-photo{position:absolute;border-radius:50%;padding:3px;background:var(--rainbow)}
  .ring-photo .inner{width:100%;height:100%;border-radius:50%;border:4px solid var(--white)}

  /* page 3 */
  .p3{left:304px;top:1905px;width:424px;height:545px}
  .p3 .tier-strip{inset:0;background:var(--purple);clip-path:polygon(170px 172px,100% 130px,100% 146px,170px 188px)}
  .p3 .red-zone{inset:0;background:var(--coral);clip-path:polygon(0 380px,100% 330px,100% 100%,0 100%)}
  .tier-badge{position:absolute;border-radius:50%;display:flex;flex-direction:column;align-items:center;justify-content:center}
  .tier-badge .name{font-family:"Rubik",Arial,sans-serif;font-weight:800;font-size:17px;line-height:18px}
  .tier-badge .price{font-family:"Rubik",Arial,sans-serif;font-weight:700;font-size:15px;line-height:18px}
  .badge-presenting{left:39px;top:95px;width:124px;height:124px;background:var(--rainbow);padding:2px}
  .badge-presenting .face{width:100%;height:100%;border-radius:50%;background:var(--white);display:flex;flex-direction:column;align-items:center;justify-content:center}
  .badge-presenting .name{background:var(--rainbow);-webkit-background-clip:text;background-clip:text;color:transparent}
  .badge-red{left:271px;top:315px;width:90px;height:90px;background:var(--coral);border:3px solid var(--white);box-shadow:0 0 0 2px var(--coral);color:var(--white)}
  .perks{list-style:none;font-size:5.8px;line-height:12px;color:var(--ink)}
  .perks li{position:relative;padding-left:9px}
  .perks li::before{content:"";position:absolute;left:0;top:4px;width:3px;height:3px;border-radius:50%;border:1px solid var(--purple)}
  .perks.light{color:var(--white)}
  .perks.light li::before{border-color:var(--white)}
</style>
</head>
<body>
<div class="board">
  <div class="board-band"></div>

  <!-- cover -->
  <section class="sheet cover" aria-label="Cover">
    <div class="dot" style="left:85px;top:45px;width:68px;height:68px;background:var(--yellow)"></div>
    <svg class="abs" style="left:0;top:0" width="370" height="478" viewBox="0 0 370 478" aria-hidden="true">
      <defs>
        <linearGradient id="coverArc" x1="0" y1="0" x2="1" y2="1">
          <stop offset="0" stop-color="#4b3a86"/><stop offset="1" stop-color="#b28cc6"/>
        </linearGradient>
      </defs>
      <path d="M 200 70 A 122 122 0 1 0 300 260" fill="none" stroke="url(#coverArc)" stroke-width="20"/>
      <circle cx="185" cy="190" r="100" fill="none" stroke="#fff" stroke-width="10"/>
    </svg>
    <div class="photo" role="img" aria-label="Photo of the state house at dusk with rainbow-lit columns" style="left:100px;top:105px;width:170px;height:170px;border-radius:50%;background:radial-gradient(circle at 50% 35%,#f1b2c4,#9b7fb5 55%,#4d5f6e)"></div>
    <div class="dot" style="left:183px;top:228px;width:112px;height:112px;background:#8a6ab0;opacity:.95"></div>
    <div class="cover-year abs" style="left:193px;top:250px;width:92px">
      <div class="year">2020</div>
      <div class="sub">PARTNER &amp;<br>SPONSORSHIP<br>OPPORTUNITIES</div>
    </div>
    <div class="brand abs" style="left:22px;top:395px">Harborlight Unity Collective</div>
    <div class="brand-rule abs" style="left:150px;top:394px"></div>
    <div class="event-line abs" style="left:160px;top:396px;width:190px">
      <b>44TH ANNUAL HARBORLIGHT GLOWFAIR &amp; ILLUMINATED NIGHT PARADE</b><br><i>SATURDAY, JUNE 20, 2020.</i>
    </div>
    <div class="cover-bottom abs"></div>
  </section>

  <!-- page 1 -->
  <div class="page-label" style="top:1094px">PAGE 1</div>
  <section class="sheet p1" aria-label="Welcome letter">
    <div class="photo" role="img" aria-label="Photo of a colourful street mural with rainbow flags along a city bridge" style="inset:0;clip-path:polygon(0 0,100% 0,100% 180px,0 232px);background:linear-gradient(120deg,#7a5a48,#d98c3a 35%,#e85d4a 55%,#5e8a52 75%,#8b6a5a)"></div>
    <div class="dot" style="left:127px;top:167px;width:66px;height:66px;background:#f7696e;opacity:.92"></div>
    <div class="dot" style="left:111px;top:227px;width:12px;height:12px;background:var(--yellow)"></div>
    <h1 class="h-display abs title">Thank you,<br>Sponsor!</h1>
    <div class="abs salute">Dear Harborlight Unity Collective Supporter,</div>
    <div class="abs copy col-left">
      <p>Thank you for taking the time to review our sponsorship package and for considering to support Harborlight Unity Collective and our 44th Annual Harborlight GlowFair and Illuminated Night Parade on Saturday, June 20, 2020.</p>
      <p>Harborlight Unity Collective brings together the greater LGBTQIA+ community to commemorate our diverse heritage, foster inclusion, educate and create awareness of issues, and celebrate achievements in equality. We create and host events that are open and inviting to everyone in the community, providing a safe environment in which individuals feel free to celebrate their relationships. Harborlight Unity Collective is committed to supporting, promoting, and collaborating with community groups in service to the greater LGBTQIA+ community. We are proud of having over four and a half decades of service to our community, advocating for equality and endeavoring to build culturally rich LGBTQIA+ Harborlight</p>
    </div>
    <div class="abs copy col-right">
      <p>Bay. Proud of our legacy and long-standing work in Harborlight Bay, we acknowledge that our success would not be possible without your generosity!</p>
      <p>When you partner with the Harborlight Unity Collective - Harborlight Bay's oldest and most comprehensive LGBTQIA+ community focused non-profit, you are making an important statement about your stance on inclusive practice, acceptance and the importance of a diverse Harborlight Bay. You are sending an affirming and significant message to the LGBTQIA+ community, your customers, employees and colleagues.</p>
      <p>GlowFair is the perfect opportunity for you to brand, market and give your company presence to over 100,000+ event goers throughout the duration of the month's events. This year, a combination of marketing channels such as social media, print, website/web links, and visual marketing will be utilized to increase the visibility of our Pride partners.</p>
      <p>Please find the sponsorship opportunities included with this letter and let us know if you have any questions, comments, or suggestions. We would appreciate the chance to provide any details that may help in deciding your sponsorship.</p>
      <p><i>Yours in Pride,</i></p>
      <p class="sign">Dale Morrow<br>Treasurer</p>
    </div>
    <svg class="abs" style="left:0;top:0" width="428" height="550" viewBox="0 0 428 550" aria-hidden="true">
      <circle cx="362" cy="552" r="58" fill="none" stroke="var(--yellow)" stroke-width="26"/>
    </svg>
  </section>

  <!-- page 2 -->
  <div class="page-label" style="top:2063px">PAGE 2</div>
  <section class="sheet p2" aria-label="Why sponsor">
    <div class="abs grey"></div>
    <div class="photo" role="img" aria-label="Photo of smiling festival-goers in sunglasses and rainbow beads" style="inset:0;clip-path:polygon(0 0,100% 0,100% 135px,0 170px);background:linear-gradient(100deg,#7fa7c9,#c9d8e6 35%,#e7c6a6 55%,#6f9bc4 80%,#a34a42)"></div>
    <div class="ring-photo" style="left:233px;top:97px;width:160px;height:160px">
      <div class="inner" role="img" aria-label="Photo of a parade-goer drinking from a bottle holding a rainbow flag" style="background:linear-gradient(160deg,#9cc8e8,#5b7f98 60%,#3a3f46)"></div>
    </div>
    <h2 class="h-display abs h-support">Support the community &amp;<br>promote your business</h2>
    <p class="abs copy para-support">Our 44th GlowFair and Illuminated Night Parade will be held on June 20, 2020 in Harborlight Bay's capitol city of Lantern City. As Harborlight Bay's largest and most recognized LGBTQIA+ organization, we are pumped to invite you to become a sponsor of this annual celebration of diversity and Pride. Official Harborlight Unity Collective events are held starting in late May and run throughout the month of June officially proclaimed Pride Month in Harborlight Bay.</p>
    <div class="dot" style="left:224px;top:248px;width:42px;height:42px;background:var(--yellow)"></div>
    <div class="dot" style="left:212px;top:301px;width:16px;height:16px;background:var(--coral)"></div>
    <div class="ring-photo" style="left:26px;top:327px;width:140px;height:140px">
      <div class="inner" role="img" aria-label="Photo of two friends in caps laughing at a festival" style="background:linear-gradient(150deg,#c9dbe8,#e0c4ae 50%,#b6473f)"></div>
    </div>
    <h2 class="h-display abs h-build">Build customer awareness<br>and loyalty</h2>
    <p class="abs copy para-build">70% OF LGBT ADULTS stated they would pay a premium for a product from a company that supports the LGBT community. Harborlight GlowFair and Illuminated Night Parade sponsors and production partners receive a tremendous amount of brand exposure both through direct and indirect marketing.</p>
    <div class="abs terms"></div>
    <div class="abs terms-head">TERMS &amp;<br>CONDITIONS</div>
    <p class="abs terms-copy">Sponsorship agreements and qualifying payment must be made by June 1, 2020 in order to receive full benefits. Sponsors receiving advertising benefits must completed their qualifying payment by April 19, 2020, sponsors are also required to send their logo artwork/ad files no later than this date to be included in the Harborlight GlowGuide – see advertising guidelines for details.</p>
  </section>

  <!-- page 3 -->
  <div class="page-label" style="top:2790px">PAGE 3</div>
  <section class="sheet p3" aria-label="Sponsorship tiers">
    <div class="photo" role="img" aria-label="Photo of a cheering parade crowd waving rainbow flags" style="inset:0;clip-path:polygon(0 0,100% 0,100% 128px,0 195px);background:linear-gradient(100deg,#3b3340,#b5546a 30%,#6f86c4 55%,#e0a45c 75%,#7a3d6a)"></div>
    <div class="abs tier-strip"></div>
    <div class="tier-badge badge-presenting">
      <div class="face">
        <div class="name">PRESENTING</div>
        <div class="price">$25,000</div>
      </div>
    </div>
    <ul class="perks abs" style="left:21px;top:232px;width:195px">
      <li>10 x 20 premium vendor booth during GlowFair</li>
      <li>Premium choice placement in the Illuminated Night Parade</li>
      <li>Use of the annual theme and Harborlight logo</li>
      <li>Click-thru logo placement on sponsorship web page</li>
      <li>Admission for six to the Harborlight VIP Party</li>
      <li>Name/logo displayed at official Harborlight events</li>
      <li>Opportunity for ad placement on harborlightunity.org homepage</li>
      <li>Opportunity to table and promote brand at key Countdown to Pride events</li>
    </ul>
    <ul class="perks abs" style="left:223px;top:172px;width:190px">
      <li>One dedicated social media post (sponsor responsible for marketing materials)</li>
      <li>Click-thru logo included in one Pre-Pride E-Blast</li>
      <li>Choice ad placement in the official Harborlight GlowGuide (back cover, inside front, back cover or inside page)</li>
      <li>Special recognition in one regional media release</li>
      <li>Special recognition at Harborlight Honors Gala</li>
      <li>Admission for Two to the mainstage entertainment meet &amp; greet</li>
      <li>Name recognition/logo placement on Harborlight Honors parade awards 2020</li>
    </ul>
    <div class="abs red-zone"></div>
    <div class="tier-badge badge-red">
      <div class="name">RED</div>
      <div class="price">$15,000</div>
    </div>
    <ul class="perks light abs" style="left:21px;top:413px;width:195px">
      <li>10 x 20 premium vendor booth during GlowFair</li>
      <li>Premium choice placement in the Illuminated Night Parade</li>
      <li>Use of the annual theme and Harborlight logo</li>
      <li>Click-thru logo placement on sponsorship web page</li>
      <li>Admission for six to the Harborlight VIP Party</li>
      <li>Name/logo displayed at official Harborlight events</li>
      <li>Opportunity for ad placement on harborlightunity.org homepage</li>
    </ul>
    <ul class="perks light abs" style="left:223px;top:413px;width:190px">
      <li>Opportunity to table and promote brand at key Countdown to Pride events</li>
      <li>One dedicated social media post (sponsor responsible for marketing materials)</li>
      <li>Click-thru logo included in one Pre-Pride E-Blast</li>
      <li>Choice ad placement in the official Harborlight GlowGuide (back cover, inside front, back cover or inside page)</li>
      <li>Special recognition in one regional media release</li>
    </ul>
  </section>
</div>
</body>
</html>
```